Professional Package for CPA Firm

We would like a stationery design for our new CPA Firm based in Atlanta, GA called 'Vale 8'. We work with investors to help grow investments, tax free. We would like the design to have a professional/minimal look with a 'wow' factor. We need 9.5″ x 4.125″, 9x12, and 10x13 mailing envelopes, business cards, and a letterhead. We have a logo that is already complete. For the letterhead, we would like to have space to put credentials at the bottom of the page

Industry/Entity Type

CPA, Accounting

```html
<!DOCTYPE html>
<html lang="en">
<head>
<meta charset="utf-8">
<title>Vale 8 Stationery</title>
<link rel="stylesheet" href="https://fonts.googleapis.com/css2?family=Montserrat:wght@300;400;500;700&family=Arimo:wght@400;700&display=swap">
<style>
:root{
  --navy:#022d3c;
  --red:#f4434c;
  --ink:#3a3a3a;
  --muted:#8c8c8c;
  --stage:#a9a9a9;
  --paper:#ffffff;
  --paper-fade:#efeff1;
}
*{box-sizing:border-box;margin:0;padding:0}
html,body{width:849px;height:1200px;overflow:hidden}
body{background:var(--stage);position:relative;font-family:"Montserrat",sans-serif;color:var(--ink)}
.sheet{position:absolute;background:linear-gradient(90deg,var(--paper-fade),var(--paper) 60%);box-shadow:0 1px 3px rgba(0,0,0,.35);overflow:hidden}

/* footer band: flat navy base with a thin red rule above */
.footer-band{position:absolute;left:0;bottom:0;width:100%;height:var(--band,14px);background:var(--navy)}
.footer-band::before{content:"";position:absolute;left:0;right:0;bottom:calc(100% + var(--gap,3px));height:var(--rule,3px);background:var(--red)}

.brand{position:absolute;color:var(--navy)}
.brand-name{display:flex;align-items:center;gap:.3em;font-weight:700;line-height:1;letter-spacing:.01em;white-space:nowrap}
.brand-dot{width:.55em;height:.55em;border-radius:50%;background:var(--red);flex:none}
.brand-tag{font-weight:500;white-space:nowrap;margin-top:.35em}
.brand-address{font-family:"Arimo",sans-serif;color:var(--muted);line-height:1.35;white-space:nowrap}

/* business card front */
.card-front{left:123px;top:32px;width:289px;height:165px;background:var(--paper)}
.card-front .brand{left:38px;top:74px}
.card-front .brand-name{font-size:24px}
.card-front .brand-tag{font-size:7.6px}
.card-front .footer-band{--band:11px;--gap:3px;--rule:3px}
.card-divider{position:absolute;left:144px;top:38px;width:1px;height:90px;background:#cfcfcf}
.card-contact{position:absolute;left:157px;top:38px;font-family:"Arimo",sans-serif;font-size:7.6px;color:#6d6d6d;line-height:1.3}
.card-contact .person{font-size:9.6px;color:var(--red);font-weight:700;letter-spacing:.02em;line-height:1.1}
.card-contact .role{margin-bottom:8px}
.card-contact .address{margin-bottom:8px}
.contact-line{display:flex;align-items:center;gap:5px;white-space:nowrap}
.icon{width:7px;height:7px;flex:none}
.icon *{fill:var(--red)}

/* business card back */
.card-back{left:452px;top:32px;width:289px;height:165px;background:var(--navy)}
.card-back .brand{left:20px;top:92px;color:#fff}
.card-back .brand-name{font-size:27px}
.card-back .brand-tag{font-size:8.4px}

/* letterhead */
.letterhead{left:37px;top:225px;width:379px;height:535px}
.letterhead .brand{left:24px;top:42px}
.letterhead .brand-name{font-size:13px}
.letterhead .brand-tag{font-size:4px}
.letterhead .footer-band{--band:18px;--gap:4px;--rule:4px}
.lh-contact{position:absolute;left:284px;top:18px;font-family:"Arimo",sans-serif;font-size:5.6px;color:#555;line-height:1.35}
.lh-contact .address{margin-bottom:4px}
.lh-contact .contact-line{gap:3px}
.lh-contact .icon{width:5px;height:5px}
.lh-rule{position:absolute;left:24px;top:66px;width:329px;height:1px;background:#9a9a9a}
.letter{position:absolute;left:38px;top:117px;width:302px;font-size:5.1px;color:var(--muted);line-height:1.32}
.letter-to{font-size:7px;letter-spacing:.15em;color:#444}
.letter-date{position:absolute;right:0;top:2px;font-size:5.2px;color:#777}
.recipient-name{font-size:6.3px;color:var(--red);margin-top:4px;margin-bottom:2px}
.recipient-lines{line-height:1.62;margin-bottom:20px}
.letter-body p{text-align:justify;margin-bottom:7px}
.signature{width:66px;height:13px;margin-top:30px;background:linear-gradient(90deg,#e7e7e9,#f3f3f4);border-radius:2px}
.signer{font-size:6.3px;color:#333;margin-top:6px}
.signer-role{font-size:4.8px;color:var(--muted)}

/* large envelopes */
.env-9x12{left:456px;top:225px;width:354px;height:460px}
.env-9x12 .brand{left:21px;top:32px}
.env-10x13{left:456px;top:730px;width:336px;height:425px}
.env-10x13 .brand{left:18px;top:33px}
.env-9x12 .brand-name,.env-10x13 .brand-name{font-size:18px}
.env-9x12 .brand-tag,.env-10x13 .brand-tag{font-size:5.3px}
.env-9x12 .brand-address,.env-10x13 .brand-address{font-size:4.9px;margin-top:6px}
.env-9x12 .footer-band,.env-10x13 .footer-band{--band:16px;--gap:4px;--rule:4px}

/* #10 envelope front */
.env-front{left:28px;top:794px;width:387px;height:168px}
.env-front .brand{left:12px;top:28px}
.env-front .brand-name{font-size:12px}
.env-front .brand-tag{font-size:3.8px}
.env-front .brand-address{font-size:4.9px;margin-top:6px}
.env-front .footer-band{--band:16px;--gap:4px;--rule:4px}

/* #10 envelope back */
.env-back{left:28px;top:987px;width:387px;height:168px}
.env-flap{position:absolute;left:0;top:0;width:100%;height:50px;display:block}
.env-back .brand{left:50%;top:14px;transform:translateX(-50%);text-align:center}
.env-back .brand-name{font-size:9px;justify-content:center}
.env-back .brand-tag{font-size:2.6px}
</style>
</head>
<body>

<section class="sheet card-front">
  <div class="brand">
    <div class="brand-name"><span class="brand-dot"></span>Vale 8</div>
    <div class="brand-tag">CPAS and Tax Advisors</div>
  </div>
  <div class="card-divider"></div>
  <div class="card-contact">
    <div class="person">DANIEL REED</div>
    <div class="role">Manager</div>
    <div class="address">Your address, city<br>state, ZIP 0000</div>
    <div class="contact-line"><svg class="icon" viewBox="0 0 10 10"><path d="M2 1l2 2-1 1.2c.6 1.2 1.6 2.2 2.8 2.8L7 6l2 2-1.3 1.3C4.5 9 1 5.5.7 2.3z"/></svg>555-010-2100</div>
    <div class="contact-line"><svg class="icon" viewBox="0 0 10 10"><path d="M0 2h10v6H0z"/></svg>hello@vale8.com</div>
    <div class="contact-line"><svg class="icon" viewBox="0 0 10 10"><circle cx="5" cy="5" r="4.6"/></svg>www.vale8.com</div>
  </div>
  <div class="footer-band"></div>
</section>

<section class="sheet card-back">
  <div class="brand">
    <div class="brand-name"><span class="brand-dot"></span>Vale 8</div>
    <div class="brand-tag">CPAS and Tax Advisors</div>
  </div>
</section>

<section class="sheet letterhead">
  <div class="brand">
    <div class="brand-name"><span class="brand-dot"></span>Vale 8</div>
    <div class="brand-tag">CPAS and Tax Advisors</div>
  </div>
  <div class="lh-contact">
    <div class="address">Your address, city<br>state, ZIP 0000</div>
    <div class="contact-line"><svg class="icon" viewBox="0 0 10 10"><path d="M2 1l2 2-1 1.2c.6 1.2 1.6 2.2 2.8 2.8L7 6l2 2-1.3 1.3C4.5 9 1 5.5.7 2.3z"/></svg>555-010-2100</div>
    <div class="contact-line"><svg class="icon" viewBox="0 0 10 10"><path d="M0 2h10v6H0z"/></svg>hello@vale8.com</div>
    <div class="contact-line"><svg class="icon" viewBox="0 0 10 10"><circle cx="5" cy="5" r="4.6"/></svg>www.vale8.com</div>
  </div>
  <div class="lh-rule"></div>

  <div class="letter">
    <div class="letter-date">Friday, 01/01/2018</div>
    <div class="letter-to">TO</div>
    <div class="recipient-name">Clara Voss</div>
    <div class="recipient-lines">Human Resources<br>Northwind Ltd.<br>48 Orchard Row, Fairmont<br>K27 USA</div>
    <div class="letter-body">
      <p>Lorem ipsum dolor sit amet, consectetuer adipiscing elit, sed diam nonummy nibh euismod tincidunt ut laoreet dolore magna aliquam erat volutpat. Ut wisi enim ad minim veniam, quis nostrud exerci tation ullamcorper suscipit lobortis nisl ut aliquip ex ea commodo consequat. Duis autem vel eum iriure dolor in hendrerit in vulputate velit esse molestie consequat.</p>
      <p>Nam liber tempor cum soluta nobis eleifend option congue nihil imperdiet doming id quod mazim placerat facer possim assum.</p>
      <p>Est usus legentis in iis qui facit eorum claritatem.</p>
      <p>Investigationes demonstraverunt lectores legere me lius quod ii legunt saepius. Claritas est etiam processus dynamicus, qui sequitur mutationem consuetudium lectorum.</p>
      <p>Consectetuer adipiscing elit, sed diam nonummy nibh euismod tincidunt ut laoreet dolore magna aliquam erat volutpat. Ut wisi enim ad minim veniam, quis nostrud exerci tation.</p>
      <p>Nam liber tempor cum soluta nobis eleifend option congue nihil imperdiet.</p>
    </div>
    <div class="signature" role="img" aria-label="Handwritten signature of Owen Hale"></div>
    <div class="signer">Owen Hale</div>
    <div class="signer-role">Managing Director</div>
  </div>
  <div class="footer-band"></div>
</section>

<section class="sheet env-9x12">
  <div class="brand">
    <div class="brand-name"><span class="brand-dot"></span>Vale 8</div>
    <div class="brand-tag">CPAS and Tax Advisors</div>
    <div class="brand-address">Your address, city<br>state, ZIP 0000</div>
  </div>
  <div class="footer-band"></div>
</section>

<section class="sheet env-10x13">
  <div class="brand">
    <div class="brand-name"><span class="brand-dot"></span>Vale 8</div>
    <div class="brand-tag">CPAS and Tax Advisors</div>
    <div class="brand-address">Your address, city<br>state, ZIP 0000</div>
  </div>
  <div class="footer-band"></div>
</section>

<section class="sheet env-front">
  <div class="brand">
    <div class="brand-name"><span class="brand-dot"></span>Vale 8</div>
    <div class="brand-tag">CPAS and Tax Advisors</div>
    <div class="brand-address">Your address, city<br>state, ZIP 0000</div>
  </div>
  <div class="footer-band"></div>
</section>

<section class="sheet env-back">
  <svg class="env-flap" viewBox="0 0 387 50" preserveAspectRatio="none" aria-hidden="true">
    <defs>
      <filter id="flap-shadow" x="-5%" y="-20%" width="110%" height="160%">
        <feDropShadow dx="0" dy="2" stdDeviation="2" flood-color="#000" flood-opacity=".22"/>
      </filter>
    </defs>
    <path d="M3 0 L8 28 Q10 45 28 46 L359 46 Q377 45 379 28 L385 0 Z" fill="#fafafa" filter="url(#flap-shadow)"/>
  </svg>
  <div class="brand">
    <div class="brand-name"><span class="brand-dot"></span>Vale 8</div>
    <div class="brand-tag">CPAS and Tax Advisors</div>
  </div>
</section>

</body>
</html>
```